Brett Olsen Building Business Card Design

Hi,

I need a business card for my Building company.
I am a Builder and build homes for clients.
I am looking for a sophisticated logo that can be used on business cards, envelopes and letter heads.
I am trying to take my business to the next level and need a professional business card.

Colours: Please use white, black, dark grey and bright blue.

Thank you,

Carol and Brett.

Target Market(s)

1. Home and Building Companies 2. Potential customers

Industry/Entity Type

Business

Contact Information for Business Card

Brett Olsen Building PTY LTD

Brett Olsen

Director

A.B.N. 37 829 516 073

BUILDERS LICENCE No. 573019k

Mobile: 0412 907 381

Email: brettolsenbuilding@mailvane.com.au

Requirements
Must have
• The following is compulsory to have in the designs:

Brett Olsen Building PTY LTD (business name)

Brett Olsen (contact name)

Director (position)

A.B.N. 37 829 516 073

Builders Licence No. 573019k

Mobile: 0412 907 381

Nice to have
• Logo for business
Should not have
• Should not be cluttered.

I am looking for a clean, sophisticated and professional business card design.

```html
<!DOCTYPE html>
<html lang="en">
<head>
<meta charset="utf-8">
<title>Brett Olsen Building – Business Card</title>
<link rel="stylesheet" href="https://fonts.googleapis.com/css2?family=Open+Sans:ital,wght@0,400;0,700;0,800;1,400&display=swap">
<style>
  :root {
    --page: #ffffff;
    --blue-deep: #0a5cd6;
    --blue-mid: #1f86ee;
    --white: #ffffff;
  }
  * { margin: 0; padding: 0; box-sizing: border-box; }
  html, body {
    width: 1200px;
    height: 694px;
    overflow: hidden;
    background: var(--page);
    font-family: "Open Sans", Arial, sans-serif;
  }
  .canvas {
    position: relative;
    width: 1200px;
    height: 694px;
  }
  .card {
    position: absolute;
    left: 18px;
    top: 20px;
    width: 1166px;
    height: 668px;
    border-radius: 28px;
    overflow: hidden;
    background:
      radial-gradient(ellipse 70% 60% at 85% 5%, rgba(120, 210, 255, 0.55), transparent 70%),
      linear-gradient(160deg, var(--blue-mid) 0%, var(--blue-deep) 55%, var(--blue-mid) 100%);
    box-shadow: 0 2px 6px rgba(0, 0, 0, 0.25);
  }
  .brand {
    position: absolute;
    left: 50px;
    top: 180px;
    display: flex;
    align-items: center;
    gap: 22px;
  }
  .brand-dot {
    width: 64px;
    height: 64px;
    border-radius: 50%;
    background: var(--white);
    flex: none;
  }
  .brand-name {
    width: 300px;
    font-size: 34px;
    font-weight: 700;
    line-height: 1.2;
    color: var(--white);
  }
  .name {
    position: absolute;
    left: 490px;
    top: 132px;
    font-size: 84px;
    font-weight: 800;
    letter-spacing: 11px;
    color: var(--white);
    line-height: 1;
    white-space: nowrap;
  }
  .title-bar {
    position: absolute;
    left: 476px;
    top: 228px;
    width: 490px;
    height: 30px;
    background: linear-gradient(90deg, rgba(255,255,255,0) 0%, rgba(255,255,255,0.85) 70%, var(--white) 100%);
  }
  .title {
    position: absolute;
    left: 974px;
    top: 222px;
    font-size: 40px;
    font-style: italic;
    color: var(--white);
    line-height: 1;
  }
  .details {
    position: absolute;
    left: 490px;
    top: 424px;
    color: var(--white);
    list-style: none;
  }
  .details li {
    display: flex;
    align-items: center;
    font-size: 34px;
    line-height: 52px;
    white-space: nowrap;
  }
  .details .phone { font-size: 44px; font-weight: 700; letter-spacing: 2px; line-height: 56px; }
  .fade-bar {
    display: inline-block;
    height: 28px;
    margin-left: 8px;
    background: linear-gradient(90deg, var(--white) 0%, rgba(255,255,255,0.6) 60%, rgba(255,255,255,0) 100%);
  }
  .abn .fade-bar { width: 300px; }
  .phone .fade-bar { width: 320px; height: 34px; }
</style>
</head>
<body>
<div class="canvas">
  <div class="card">
    <div class="brand">
      <span class="brand-dot"></span>
      <span class="brand-name">Brett Olsen Building PTY LTD</span>
    </div>
    <h1 class="name">Brett Olsen</h1>
    <div class="title-bar"></div>
    <p class="title">Director</p>
    <ul class="details">
      <li class="abn">A.B.N. 37 829 516 073<span class="fade-bar"></span></li>
      <li class="licence">Builders Licence No. 573019k</li>
      <li class="phone">0412 907 381<span class="fade-bar"></span></li>
      <li class="email">brettolsenbuilding@mailvane.com.au</li>
    </ul>
  </div>
</div>
</body>
</html>
```